Venlox - Property Management Company Listings - PSD / uncoded only

Our site simply connects property owners with property managers. I’m asking you to create 2 pages, 1 homepage and 1 page that lists of property management companies. Build with Responsive Design in mind. PSD/uncoded files only. Help us create a great site!
Example competitor sites:
http://www.everyestatehelp.example/
http://www.tendyourlots.example/
Inspired by these sites:
http://www.quorvik.example/
http://www.bespokely.example/
http://www.coinwire.example/
https://www.tripboard.example/
I've attached the logo as well as 2 picture files that you can consider using.
• Venlox Logo Colors: Yellow: HTML code: #FBC30A, RGB code: R: 251 G: 195 B: 10 Grey: HTML code: #4E4C4D, RGB code: R: 78 G: 76 B: 77
• The picture files are optional.
o One picture is of houses and neighborhood.
o The other is of a professional woman on the phone. Please do not use the professional woman as a large primary image. You can use the professional woman photo as a smaller photo and not the main photo.
• Please bring your own pictures and graphics too. Don't feel like you need to use mine.
Thank you!

```html
<!DOCTYPE html>
<html lang="en">
<head>
<meta charset="utf-8">
<title>Venlox – Find your Local Property Manager</title>
<link href="https://fonts.googleapis.com/css2?family=Roboto:wght@300;400;500;700&display=swap" rel="stylesheet">
<style>
  :root {
    --brand-yellow: #fbc30a;
    --brand-grey: #4e4c4d;
    --ink: #3f3f3f;
    --ink-soft: #555555;
    --white: #ffffff;
    --button-dark: #3b3b3b;
    --panel-yellow: rgba(235, 185, 10, 0.82);
  }
  * { box-sizing: border-box; margin: 0; padding: 0; }
  html, body { width: 1200px; height: 899px; overflow: hidden; }
  body {
    font-family: "Roboto", Arial, sans-serif;
    background: var(--white);
    color: var(--ink);
    position: relative;
  }

  .site-header {
    position: absolute; left: 0; top: 0; width: 1200px; height: 56px;
    background: linear-gradient(#ffffff, #f1f1f1);
    border-bottom: 1px solid #e2e2e2;
  }
  .brand {
    position: absolute; left: 150px; top: 10px;
    display: flex; align-items: center; gap: 8px;
  }
  .brand-mark { width: 12px; height: 12px; background: var(--brand-yellow); }
  .brand-name {
    font-size: 30px; font-weight: 700; color: var(--brand-grey);
    letter-spacing: -0.5px; line-height: 36px;
  }
  .tagline {
    position: absolute; right: 122px; top: 19px;
    font-size: 14px; color: #2e2e2e;
  }
  .tagline em { font-style: normal; color: var(--brand-yellow); }

  .hero {
    position: absolute; left: 0; top: 56px; width: 1200px; height: 552px;
  }
  .hero-photo {
    position: absolute; inset: 0;
    background:
      radial-gradient(ellipse at 62% 40%, rgba(180,120,80,0.55), transparent 55%),
      linear-gradient(180deg, #6b625a 0%, #4a423c 45%, #2b2623 75%, #1f1b19 100%);
  }
  .hero-title {
    position: absolute; left: 0; right: 0; top: 168px;
    text-align: center; color: var(--white);
    font-size: 29px; font-weight: 500; letter-spacing: -0.2px;
    text-shadow: 0 1px 3px rgba(0,0,0,0.5);
  }
  .search-panel {
    position: absolute; left: 288px; top: 239px; width: 632px; height: 77px;
    background: var(--panel-yellow);
  }
  .field-label {
    position: absolute; top: 10px; font-size: 12px; color: #2b2b2b;
  }
  .select-box {
    position: absolute; left: 33px; top: 30px; width: 296px; height: 34px;
    background: var(--white); border: 1px solid #ddd;
    font-size: 12px; color: #888; padding: 9px 0 0 11px;
  }
  .select-box::after {
    content: ""; position: absolute; right: 15px; top: 15px;
    border-left: 3px solid transparent; border-right: 3px solid transparent;
    border-top: 4px solid #333;
  }
  .zip-box {
    position: absolute; left: 346px; top: 30px; width: 100px; height: 34px;
    background: var(--white); border: 1px solid #ddd;
  }
  .search-button {
    position: absolute; left: 463px; top: 30px; width: 136px; height: 34px;
    background: var(--button-dark); color: var(--white);
    font-size: 13px; font-weight: 500;
    display: flex; align-items: center; justify-content: center; gap: 8px;
  }
  .hero-note {
    position: absolute; left: 0; right: 0; top: 334px; text-align: center;
    font-size: 13px; font-weight: 300; color: var(--white);
  }

  .steps-heading {
    position: absolute; left: 0; right: 0; top: 659px; text-align: center;
    font-size: 23px; color: var(--ink);
  }
  .step {
    position: absolute; top: 743px; width: 300px; text-align: center;
  }
  .step-icon { display: block; margin: 0 auto; }
  .step-label {
    margin-top: 16px; font-size: 13px; font-weight: 500; color: var(--ink-soft);
  }
</style>
</head>
<body>
  <header class="site-header">
    <div class="brand">
      <span class="brand-mark"></span>
      <span class="brand-name">Venlox</span>
    </div>
    <p class="tagline">Property Management Solutions, <em>Simplified.</em></p>
  </header>

  <section class="hero">
    <div class="hero-photo" role="img" aria-label="Busy city shopping street at dusk with crowds of pedestrians and stone buildings"></div>
    <h1 class="hero-title">Find your Local Property Manager</h1>
    <form class="search-panel">
      <span class="field-label" style="left:45px">Select Your Property Type</span>
      <div class="select-box">Single Home or Condo (Valued up to $300K)</div>
      <span class="field-label" style="left:358px">In Zipcode</span>
      <div class="zip-box"></div>
      <div class="search-button">
        <svg width="12" height="12" viewBox="0 0 12 12"><circle cx="5" cy="5" r="3.5" fill="none" stroke="#fbc30a" stroke-width="1.8"/><line x1="7.6" y1="7.6" x2="11" y2="11" stroke="#fbc30a" stroke-width="2"/></svg>
        Search Now
      </div>
    </form>
    <p class="hero-note">Search our directory to find experienced and professional property management companies that meet your needs.</p>
  </section>

  <h2 class="steps-heading">To find property management companies near you:</h2>

  <div class="step" style="left:127px">
    <svg class="step-icon" width="78" height="78" viewBox="0 0 78 78">
      <circle cx="39" cy="39" r="37" fill="#fff" stroke="#4e4c4d" stroke-width="3"/>
      <circle cx="39" cy="39" r="33" fill="#fff" stroke="#fbc30a" stroke-width="4"/>
      <path d="M30 34 L39 26 L48 34 V44 H30 Z" fill="#fbc30a" stroke="#4e4c4d" stroke-width="2"/>
      <rect x="36" y="37" width="6" height="7" fill="#4e4c4d"/>
      <path d="M20 50 Q30 46 38 50 L48 50 Q54 47 60 44 Q58 52 48 56 H28 L20 56 Z" fill="#4e4c4d"/>
    </svg>
    <p class="step-label">Select your property type and zipcode</p>
  </div>

  <div class="step" style="left:454px">
    <svg class="step-icon" width="78" height="78" viewBox="0 0 78 78">
      <circle cx="39" cy="39" r="37" fill="#fff" stroke="#4e4c4d" stroke-width="3"/>
      <circle cx="39" cy="39" r="33" fill="#fff" stroke="#fbc30a" stroke-width="4"/>
      <rect x="25" y="23" width="24" height="30" fill="#fbc30a"/>
      <line x1="29" y1="30" x2="41" y2="30" stroke="#fff" stroke-width="2"/>
      <line x1="29" y1="35" x2="38" y2="35" stroke="#fff" stroke-width="2"/>
      <line x1="29" y1="40" x2="36" y2="40" stroke="#fff" stroke-width="2"/>
      <circle cx="44" cy="41" r="7" fill="#fff" stroke="#4e4c4d" stroke-width="2.5"/>
      <line x1="49" y1="46" x2="56" y2="53" stroke="#4e4c4d" stroke-width="4" stroke-linecap="round"/>
    </svg>
    <p class="step-label">Review property manager listings in your area</p>
  </div>

  <div class="step" style="left:769px">
    <svg class="step-icon" width="78" height="78" viewBox="0 0 78 78">
      <circle cx="39" cy="39" r="37" fill="#fff" stroke="#4e4c4d" stroke-width="3"/>
      <circle cx="39" cy="39" r="33" fill="#fff" stroke="#fbc30a" stroke-width="4"/>
      <circle cx="44" cy="29" r="7" fill="#fbc30a"/>
      <rect x="35" y="37" width="18" height="19" rx="3" fill="#fbc30a"/>
      <circle cx="32" cy="34" r="6" fill="#4e4c4d"/>
      <rect x="24" y="41" width="16" height="15" rx="3" fill="#4e4c4d"/>
      <rect x="50" y="44" width="8" height="12" rx="2" fill="#4e4c4d"/>
    </svg>
    <p class="step-label">Select and compare property managers</p>
  </div>
</body>
</html>
```